The Polish & Sugar Loft Website Update

Hello. I am seeking to freshen up my website with a clean and easy feel that incorporates our modern chic style. Our services cater to mostly young professionals and modern moms.

We focus on natural nail care and gentle professional waxing. We are known for our cleanliness. Our clients like our current website, however I'm hoping to make it look even more professional and user friendly. Some clients have even said our current website feels welcoming, unlike other websites that in they feel give a snobbish vibe. I like clean lines, simple, fresh, and sometimes bold. Totally NOT a fan of whimsical.

I threw added an accent color to the color pallet...however it should be used in moderation. I am also open to other accent colors. I'd like the site to emphasize the Brazilian wax as much as nails, if not more than nail. The photos downloaded are just to give you a few images of who we are, however are not necessary. Current website www.polishsugarloft-demo.com

Target Market(s)

Females 30-55

Industry/Entity Type

Beauty Salon

Coding

Coded - Design and coding required

Number of Pages Required

5+ page

Font styles to use
Sans Serif

Colors
ffffff
1b1b1b
acd136
eeeeee
878787
c4c4c4
efefef
7f7f7f

Requirements
Must have
• Clean look
Nice to have
• Our logo
Should not have
• Whimsical

```html
<!DOCTYPE html>
<html lang="en">
<head>
<meta charset="utf-8">
<title>The Polish &amp; Sugar Loft</title>
<link rel="stylesheet" href="https://fonts.googleapis.com/css2?family=Raleway:wght@400;500;600&family=Lato:wght@400;700&display=swap">
<style>
:root{
  --white:#ffffff;
  --ink:#1b1b1b;
  --accent:#acd136;
  --mist:#eeeeee;
  --stone:#878787;
  --silver:#c4c4c4;
  --haze:#efefef;
  --slate:#7f7f7f;
  --bar:#2b2b2b;
}
*{box-sizing:border-box;margin:0;padding:0}
html,body{width:1200px;height:2835px;overflow:hidden;background:var(--white)}
body{font-family:"Lato",sans-serif;color:var(--ink);position:relative}
.heading{font-family:"Raleway",sans-serif}

/* header */
.site-header{position:absolute;top:0;left:0;width:1200px;height:114px;background:var(--white)}
.quick-link{position:absolute;top:24px;display:flex;align-items:center;gap:14px;font-size:17px;font-weight:700}
.quick-link span{font-weight:400;color:var(--stone)}
.quick-link.gift{left:48px}
.quick-link.schedule{right:48px}
.icon-ring{width:64px;height:64px;border-radius:50%;background:var(--mist);border:3px solid var(--silver);display:flex;align-items:center;justify-content:center}
.icon-dot{width:44px;height:44px;border-radius:50%;background:var(--slate);display:flex;align-items:center;justify-content:center}
.brand-name{position:absolute;top:36px;left:0;width:1200px;text-align:center;font-family:"Raleway",sans-serif;font-size:34px;font-weight:500;color:var(--ink)}

/* navigation */
.main-nav{position:absolute;top:114px;left:0;width:1200px;height:69px;background:var(--ink);display:flex;align-items:center;padding-left:52px}
.main-nav a{color:var(--white);text-decoration:none;font-size:14px;height:69px;line-height:69px;padding:0 20px;margin-right:26px}
.main-nav a.active{background:#3c3c3c}

/* hero */
.hero{position:absolute;top:183px;left:0;width:1200px;height:681px;background:linear-gradient(120deg,#d9c2b2 0%,#efe6e0 45%,#f4f1ef 70%,#e9dcd8 100%)}
.hero-copy{position:absolute;right:48px;top:390px;width:660px;text-align:right}
.hero-copy h1{font-family:"Raleway",sans-serif;font-weight:500;font-size:58px;color:#2a2a2a;margin-bottom:18px}
.hero-copy p{font-size:13.5px;line-height:22px;color:#333}
.btn-dark{display:inline-block;background:var(--bar);color:var(--white);font-size:12px;text-transform:uppercase;padding:12px 26px;text-decoration:none}
.hero-copy .btn-dark{margin-top:24px;padding:13px 28px}
.hero-dots{position:absolute;left:56px;top:565px;display:flex;gap:10px;align-items:center}
.hero-dots i{width:10px;height:10px;border-radius:50%;background:var(--ink);display:block}
.hero-dots i.current{width:20px;height:20px;border:3px solid var(--ink);background:var(--white);box-shadow:inset 0 0 0 3px var(--white);background-clip:padding-box;background-color:var(--ink)}

/* welcome */
.welcome{position:absolute;top:864px;left:0;width:1200px;height:338px;text-align:center;padding-top:38px}
.welcome h2{font-family:"Raleway",sans-serif;font-weight:500;font-size:35px;margin-bottom:22px}
.welcome p{width:960px;margin:0 auto 22px;font-size:12.5px;line-height:22px;color:var(--stone)}
.welcome .btn-dark{padding:10px 26px;text-transform:none}

/* facials */
.facials{position:absolute;top:1202px;left:0;width:1200px;height:410px;background:linear-gradient(180deg,#5a4b40 0%,#3d322b 55%,#2d2621 100%);text-align:center;color:var(--white);padding-top:80px}
.facials h2{font-family:"Raleway",sans-serif;font-weight:500;font-size:33px;margin-bottom:22px}
.facials p{width:880px;margin:0 auto 26px;font-size:15.5px;line-height:27px}
.facials .btn-black{display:inline-block;background:#0f0f0f;color:var(--white);font-size:13px;padding:18px 50px;text-transform:uppercase}

/* service menu */
.service-menu{position:absolute;top:1612px;left:0;width:1200px;height:483px}
.service-menu h2{position:absolute;left:216px;top:36px;font-family:"Raleway",sans-serif;font-weight:500;font-size:34px}
.service-menu h2 span{color:var(--stone)}
.menu-track{position:absolute;left:114px;top:100px;width:440px;height:108px}
.menu-track .line{position:absolute;left:53px;right:53px;top:53px;height:1px;background:var(--silver)}
.menu-badge{position:absolute;top:0;width:108px;height:108px;border-radius:50%;background:#2d2d2d;border:4px solid var(--white);box-shadow:0 0 0 2px var(--silver);color:var(--white);font-family:"Raleway",sans-serif;font-size:22px;display:flex;align-items:center;justify-content:center}
.menu-badge.nail{left:0}
.menu-badge.wax{right:0}
.menu-list{position:absolute;top:222px;list-style:none;font-size:16px;color:#333}
.menu-list li{height:45.5px;display:flex;align-items:center;gap:12px}
.menu-list.nail{left:64px}
.menu-list.wax{left:404px}
.nails-photo{position:absolute;left:596px;top:42px;width:604px;height:400px;background:radial-gradient(ellipse at 60% 55%,#ecc8b4 0%,#f3e1d6 45%,var(--white) 75%)}

/* appointments */
.appointments{position:absolute;top:2095px;left:0;width:1200px;height:305px;background:linear-gradient(90deg,#121212 0%,#2a2a2a 50%,#141414 100%);color:var(--white);text-align:center}
.appointments h2{font-family:"Raleway",sans-serif;font-weight:500;font-size:33px;padding-top:62px}
.appt-row{position:absolute;top:148px;left:157px;width:862px;height:65px}
.appt-row .line{position:absolute;left:0;right:0;top:32px;height:1px;background:var(--stone)}
.appt-box{position:absolute;top:0;width:304px;height:65px;background:var(--stone);font-size:13px;text-transform:uppercase;display:flex;align-items:center;justify-content:center;gap:10px}
.appt-box.available{left:0}
.appt-box.hours{right:0;width:284px}
.appt-circle{position:absolute;left:404px;top:-7px;width:80px;height:80px;border-radius:50%;border:2px solid var(--silver);background:var(--ink);display:flex;align-items:center;justify-content:center}
.appt-circle span{width:64px;height:64px;border-radius:50%;background:var(--stone);display:flex;align-items:center;justify-content:center;font-size:12px;text-transform:uppercase}
.appt-note{position:absolute;top:247px;width:1200px;font-size:12px;text-transform:uppercase}

/* contact */
.contact{position:absolute;top:2400px;left:0;width:1200px;height:386px}
.drips-art{position:absolute;left:0;top:0;width:472px;height:300px;background:linear-gradient(90deg,#f2c7bc 0%,#7a1b3c 25%,#3a1420 45%,#7a2150 62%,#d92a7a 82%,#e03050 100%);opacity:.85}
.contact-card{position:absolute;left:694px;top:66px}
.contact-card h3{font-family:"Lato",sans-serif;font-weight:400;font-size:22px;margin-bottom:10px}
.contact-card p{font-size:16px;line-height:25px;color:var(--stone)}
.contact-card p b{color:var(--ink);font-weight:400}
.contact-card .gap{margin-top:8px}
.social-row{display:flex;gap:16px;margin-top:42px}
.social-row span{width:60px;height:60px;border-radius:50%;background:var(--silver)}
.social-row span.dark{background:#050505}

/* footer */
.site-footer{position:absolute;top:2786px;left:0;width:1200px;height:49px;border-top:1px solid var(--silver);text-align:center;line-height:48px;font-size:12px;color:#333}
</style>
</head>
<body>

<header class="site-header">
  <div class="quick-link gift">
    <div class="icon-ring"><div class="icon-dot">
      <svg width="20" height="20" viewBox="0 0 20 20"><rect x="3" y="8" width="14" height="10" fill="none" stroke="#fff" stroke-width="2"/><rect x="2" y="5" width="16" height="4" fill="#fff"/><line x1="10" y1="5" x2="10" y2="18" stroke="#878787" stroke-width="2"/></svg>
    </div></div>
    Purchase Gift Cards <span>Online</span>
  </div>
  <div class="brand-name">The Polish &amp; Sugar Loft</div>
  <div class="quick-link schedule">
    Schedule <span>Online!</span>
    <div class="icon-ring"><div class="icon-dot">
      <svg width="18" height="22" viewBox="0 0 18 22"><rect x="2" y="2" width="14" height="18" rx="2" fill="none" stroke="#fff" stroke-width="2"/><line x1="6" y1="8" x2="12" y2="8" stroke="#fff" stroke-width="2"/><line x1="6" y1="13" x2="12" y2="13" stroke="#fff" stroke-width="2"/></svg>
    </div></div>
  </div>
</header>

<nav class="main-nav">
  <a class="active" href="#">Home</a>
  <a href="#">Schedule An Appointment</a>
  <a href="#">Products and Services</a>
  <a href="#">Careers</a>
  <a href="#">Specials</a>
  <a href="#">About Us</a>
  <a href="#">FAQ</a>
  <a href="#">Contact Us</a>
</nav>

<section class="hero" role="img" aria-label="Photo of a manicurist painting white and gold nail art beside a bottle of pale pink polish">
  <div class="hero-copy">
    <h1>Hot Stone Manicure</h1>
    <p>Lorem ipsum dolor sit amet, consectetur adipiscing elit, sed do eiusmod tempor incididunt ut labore et dolore magna aliqua. Ut enim ad minim veniam, quis nostrud exercitation ullamco laboris</p>
    <a class="btn-dark" href="#">Read More</a>
  </div>
  <div class="hero-dots"><i></i><i class="current"></i><i></i></div>
</section>

<section class="welcome">
  <h2>Welcome to The Polish &amp; Sugar Loft</h2>
  <p>To be the #1 nail and wax salon in the Maple Falls, CT area, offering the most meticulous manicures, pedicures, and waxing service. We use superior products, advanced techniques, and exceptional sanitation procedures to provide our clients with safe, quality services. Our knowledgeable and friendly staff is always happy to assist with any of your Polish &amp; Sugar concerns.</p>
  <p>We are excited to welcome another Licensed Nail Technician to our team, Dana Whitfield. Dana has over 25 years experience and is also a certified Medical Nail Technician. You will love her spunk and genuine friendliness. If you're seeking a perfect mani, Dana is your girl.</p>
  <a class="btn-dark" href="#">Read More</a>
</section>

<section class="facials" role="img" aria-label="Photo of pedicured feet with French tips resting on a bamboo mat with flowers">
  <h2>Facials are Now Available at The Polish &amp; Sugar Loft</h2>
  <p>Our Signature Facial is meticulously customized to your skin's needs, be it quenching your skin's thirst, clearing unflattering breakouts, or repairing sun damage and fine lines.</p>
  <span class="btn-black">Click Here</span>
</section>

<section class="service-menu">
  <h2>Service <span>Menu</span></h2>
  <div class="menu-track">
    <div class="line"></div>
    <div class="menu-badge nail">Nail</div>
    <div class="menu-badge wax">Wax</div>
  </div>
  <ul class="menu-list nail">
    <li><svg width="12" height="10" viewBox="0 0 12 10"><path d="M1 5l3.5 3.5L11 1" fill="none" stroke="#1b1b1b" stroke-width="2"/></svg>Signature Manicure- $24</li>
    <li><svg width="12" height="10" viewBox="0 0 12 10"><path d="M1 5l3.5 3.5L11 1" fill="none" stroke="#1b1b1b" stroke-width="2"/></svg>Gel Shine Manicure - $34</li>
    <li><svg width="12" height="10" viewBox="0 0 12 10"><path d="M1 5l3.5 3.5L11 1" fill="none" stroke="#1b1b1b" stroke-width="2"/></svg>Signature Pedicure - $40</li>
  </ul>
  <ul class="menu-list wax">
    <li><svg width="12" height="10" viewBox="0 0 12 10"><path d="M1 5l3.5 3.5L11 1" fill="none" stroke="#1b1b1b" stroke-width="2"/></svg>Brow Design - $13</li>
    <li><svg width="12" height="10" viewBox="0 0 12 10"><path d="M1 5l3.5 3.5L11 1" fill="none" stroke="#1b1b1b" stroke-width="2"/></svg>Chin - $10</li>
    <li><svg width="12" height="10" viewBox="0 0 12 10"><path d="M1 5l3.5 3.5L11 1" fill="none" stroke="#1b1b1b" stroke-width="2"/></svg>Lip - $10</li>
    <li><svg width="12" height="10" viewBox="0 0 12 10"><path d="M1 5l3.5 3.5L11 1" fill="none" stroke="#1b1b1b" stroke-width="2"/></svg>Brazilian $55</li>
  </ul>
  <div class="nails-photo" role="img" aria-label="Photo of a hand with glossy red manicured nails"></div>
</section>

<section class="appointments">
  <h2>SERVICES BY APPOINTMENT ONLY</h2>
  <div class="appt-row">
    <div class="line"></div>
    <div class="appt-box available">
      <svg width="16" height="16" viewBox="0 0 16 16"><rect x="1.5" y="3" width="13" height="11.5" fill="none" stroke="#fff" stroke-width="1.5"/><line x1="1.5" y1="6.5" x2="14.5" y2="6.5" stroke="#fff" stroke-width="1.5"/><line x1="5" y1="1" x2="5" y2="4" stroke="#fff" stroke-width="1.5"/><line x1="11" y1="1" x2="11" y2="4" stroke="#fff" stroke-width="1.5"/></svg>
      Appointments Available
    </div>
    <div class="appt-circle"><span>Daily</span></div>
    <div class="appt-box hours">
      <svg width="16" height="16" viewBox="0 0 16 16"><circle cx="8" cy="8" r="6.5" fill="none" stroke="#fff" stroke-width="1.5"/><path d="M8 4v4h3" fill="none" stroke="#fff" stroke-width="1.5"/></svg>
      9AM-8PM Most Days
    </div>
  </div>
  <p class="appt-note">Salon is only staffed for scheduled appointments.</p>
</section>

<section class="contact">
  <div class="drips-art" role="img" aria-label="Illustration of dripping nail polish in pink, plum and red tones"></div>
  <div class="contact-card">
    <h3>The Polish &amp; Sugar Loft</h3>
    <p><b>Ad:</b> 42 Linden Avenue<br>Maple Falls, CT 06011</p>
    <p class="gap"><b>Ph:</b> (555) 014-2287</p>
    <p class="gap"><b>Em:</b> hello@polishsugarloft-demo.com</p>
    <div class="social-row">
      <span></span><span class="dark"></span><span></span><span></span>
    </div>
  </div>
</section>

<footer class="site-footer">Company Name © 2016 Privacy Policy. Terms of use</footer>

</body>
</html>
```